Natural Organic Cosmetics needs a packaging design

I need package design designs for an organic, natural, unrefined shea butter packaged in a pouch like the example below. The package design should express pure, organic, freshness, moisturizing and healthy. The package design should also reflect the benefits of the product listed below. The product will be called “ORGANIC SHEA BUTTER”
MEANING OF NAME: ZENO AFRICA" meaning to Come to Africa for your natural cosmetics
Logo Text/Brand Name:
“ZENO”
Logo Styles of Interest:
Elegance
Natural
Organic
Freshness
Unrefined
From a tree nut
Target Market:
General public
Must have:
KISS : Keep it simple stupid
Note: I have a shea nuts stock photo i can provide.
Dimension:W = 7.48 InchesH = 10.43 inches Added Thursday, January 14, 2016
Industry/Entity Type
Cosmetics

```html
<!DOCTYPE html>
<html lang="en">
<head>
<meta charset="utf-8">
<title>ZENO Shea Butter – Pouch Front and Back</title>
<link rel="stylesheet" href="https://fonts.googleapis.com/css2?family=Archivo+Black&family=Kaushan+Script&family=Tinos:ital,wght@0,400;0,700;1,400;1,700&display=swap">
<style>
  :root {
    --stage: #646464;
    --pouch: #ffffff;
    --leaf-green: #4f8a24;
    --leaf-dark: #3c6f1a;
    --fresh-green: #8cbf3a;
    --pale-green: #dfeec8;
    --sun-yellow: #f5ee63;
    --label-yellow: #fff36a;
    --orange: #f39a1e;
    --peach: #f2d6b4;
    --text-green: #4e7e22;
    --nut-brown: #6b3a1c;
  }
  * { margin: 0; padding: 0; box-sizing: border-box; }
  html, body { width: 1200px; height: 1000px; overflow: hidden; background: var(--stage); }
  .canvas { position: relative; width: 1200px; height: 1000px; background: var(--stage); }
  .panel { position: absolute; top: 118px; width: 495px; height: 752px; background: var(--pouch); overflow: hidden; }
  .panel--front { left: 35px; }
  .panel--back { left: 660px; }
  .panel svg { position: absolute; inset: 0; }
  .abs { position: absolute; left: 0; width: 100%; text-align: center; }

  .brand-name { font-family: "Archivo Black", sans-serif; color: #fff; }
  .front-brand { top: 132px; font-size: 50px; letter-spacing: 1px; }
  .product-script { font-family: "Kaushan Script", cursive; }
  .front-product { top: 196px; font-size: 32px; color: var(--label-yellow); }
  .claims-pill {
    position: absolute; left: 125px; top: 246px; width: 250px; height: 30px;
    background: var(--orange); border: 2px solid #fff; outline: 2px solid var(--orange);
    font-family: "Tinos", serif; font-style: italic; color: #fff; font-size: 18px;
    line-height: 26px; text-align: center;
  }
  .net-weight { top: 632px; font-family: "Tinos", serif; font-weight: 700; color: var(--text-green); font-size: 20px; }
  .usage-note { top: 655px; font-family: "Tinos", serif; font-weight: 700; color: var(--text-green); font-size: 17px; }

  .back-brand { top: 24px; font-size: 42px; color: var(--label-yellow); }
  .back-product { top: 96px; font-size: 24px; color: var(--text-green); }
  .back-claims { top: 130px; font-family: "Tinos", serif; font-style: italic; font-weight: 700; font-size: 17px; color: var(--fresh-green); }
  .benefits-box {
    position: absolute; left: 43px; top: 154px; width: 425px; height: 163px;
    background: var(--peach); padding: 4px 12px;
    font-family: "Tinos", serif; font-size: 10px; line-height: 11.6px; color: #3b2a1a; text-align: center;
  }
  .disclaimer-box {
    position: absolute; left: 40px; top: 327px; width: 433px; height: 130px;
    background: var(--pale-green); padding: 2px 20px;
    font-family: "Tinos", serif; font-weight: 700; font-size: 15px; line-height: 18px; color: var(--text-green); text-align: center;
  }
  .storage-note { top: 551px; font-family: "Tinos", serif; font-weight: 700; font-size: 12.5px; line-height: 15.5px; color: #fff; }
  .company-info { top: 622px; font-family: "Tinos", serif; font-weight: 700; font-size: 14px; line-height: 17px; color: var(--text-green); }
  .company-info p + p { margin-top: 12px; }
</style>
</head>
<body>
<div class="canvas">

  <section class="panel panel--front">
    <svg viewBox="0 0 495 752" width="495" height="752">
      <defs>
        <linearGradient id="leafHaze" x1="0" y1="0" x2="1" y2="1">
          <stop offset="0" stop-color="#e8f1d6"/>
          <stop offset="0.6" stop-color="#f4f8ea"/>
          <stop offset="1" stop-color="#dbe9c4"/>
        </linearGradient>
        <linearGradient id="nutsTone" x1="0" y1="0" x2="1" y2="0">
          <stop offset="0" stop-color="#6b3a1c"/>
          <stop offset="0.32" stop-color="#8a5230"/>
          <stop offset="0.42" stop-color="#f3efe2"/>
          <stop offset="0.58" stop-color="#f3efe2"/>
          <stop offset="0.7" stop-color="#7d4524"/>
          <stop offset="1" stop-color="#5c2f16"/>
        </linearGradient>
        <linearGradient id="branchTone" x1="0" y1="0" x2="1" y2="1">
          <stop offset="0" stop-color="#3f7a1d"/>
          <stop offset="0.5" stop-color="#7fb23a"/>
          <stop offset="1" stop-color="#2f5f14"/>
        </linearGradient>
        <path id="frontSlogan" d="M20,468 Q248,415 480,452"/>
      </defs>
      <rect x="0" y="0" width="495" height="430" fill="url(#leafHaze)" role="img" aria-label="Faded shea tree leaves"/>
      <rect x="158" y="0" width="180" height="240" fill="var(--leaf-green)"/>
      <circle cx="248" cy="58" r="34" fill="#c9c66a" stroke="#fff" stroke-width="3"/>
      <path d="M0,305 L495,305 L495,440 Q248,395 0,455 Z" fill="url(#nutsTone)" role="img" aria-label="Shea nuts around a glass bowl of shea butter"/>
      <path d="M0,470 Q248,415 495,455 L495,615 Q248,585 0,615 Z" fill="url(#branchTone)" role="img" aria-label="Green shea fruit on a leafy branch"/>
      <path d="M0,445 Q248,395 495,430 L495,462 Q248,422 0,478 Z" fill="var(--sun-yellow)"/>
      <path d="M0,432 Q248,385 495,420 L495,432 Q248,397 0,446 Z" fill="var(--fresh-green)"/>
      <path d="M0,610 Q248,580 495,610 L495,626 Q248,608 0,640 Z" fill="var(--fresh-green)"/>
      <path d="M0,622 Q248,600 495,622 L495,634 Q248,618 0,650 Z" fill="var(--sun-yellow)"/>
      <text font-family="Tinos, serif" font-style="italic" font-weight="700" font-size="17" fill="var(--leaf-dark)" text-anchor="middle">
        <textPath href="#frontSlogan" startOffset="50%">Come to Africa for your Natural Cosmetics</textPath>
      </text>
    </svg>
    <div class="abs brand-name front-brand">ZENO</div>
    <div class="abs product-script front-product">Shea Butter</div>
    <div class="claims-pill">Organic • Unrefined • Natural</div>
    <div class="abs net-weight">16 OZ.</div>
    <div class="abs usage-note">External Use Only</div>
  </section>

  <section class="panel panel--back">
    <svg viewBox="0 0 495 752" width="495" height="752">
      <defs>
        <linearGradient id="backBranch" x1="0" y1="0" x2="1" y2="1">
          <stop offset="0" stop-color="#3d7a1c"/>
          <stop offset="0.5" stop-color="#5f9a2c"/>
          <stop offset="1" stop-color="#2e5c13"/>
        </linearGradient>
        <path id="storageCurve" d="M30,532 Q248,488 465,524"/>
      </defs>
      <rect x="158" y="0" width="180" height="90" fill="var(--leaf-green)"/>
      <path d="M0,460 Q248,430 495,460 L495,620 Q248,600 0,620 Z" fill="url(#backBranch)" role="img" aria-label="Shea tree leaves"/>
      <path d="M0,448 Q248,418 495,448 L495,462 Q248,432 0,462 Z" fill="var(--fresh-green)"/>
      <path d="M0,616 Q248,596 495,616 L495,628 Q248,608 0,628 Z" fill="var(--fresh-green)"/>
      <circle cx="248" cy="460" r="27" fill="#c9c66a" stroke="#fff" stroke-width="3"/>
      <text font-family="Tinos, serif" font-size="14" fill="#fff" text-anchor="middle">
        <textPath href="#storageCurve" startOffset="50%">STORE IN A COOL DRY PLACE AND AVOID DIRECT SUNLIGHT</textPath>
      </text>
    </svg>
    <div class="abs brand-name back-brand">ZENO</div>
    <div class="abs product-script back-product">Shea Butter</div>
    <div class="abs back-claims">Organic • Unrefined • Natural</div>
    <div class="benefits-box">
      <p>ZENO Shea Butter is 100% natural, unrefined and produced from an edible nut produced by the Shea Tree (Karite). This tree is commonly found in parts of Western and Central Africa including: Ghana, Mali, and Burkina Faso.</p>
      <p>Shea butter nourishes the skin with Vitamins A, E and F. Vitamins A and E maintain the skin and keep it clear and healthy. They are particularly helpful for sun damaged skin and to help prevent premature wrinkles and facial lines. The Vitamin A in shea butter is important for improving skin conditions, including blemishes, wrinkles, eczema, and dermatitis. Vitamin F acts as a protector and rejuvenator soothing rough dry or chapped skin and helps soften dry or damaged hair.</p>
      <p>The rich, creamy texture and high content of non-saponifible fats (Vitamin F) in the Shea Butter make it an ideal moisturizer. It can be added to skin care formulations or used by itself to assist with aging skin, eczema, dryness and relief from irritation. Shea Butter can also be used on the hair to moisturize a dry scalp and stimulate hair growth.</p>
    </div>
    <div class="disclaimer-box">
      Shea butter benefits listed above are generally accepted by the public as the benefits of the natural butter. These statements have not been evaluated by the FDA or other authorities. This product is not intended to diagnose, treat, cure or prevent any disease.<br>
      Products may vary slightly in color and appearance due to being all-natural products.
    </div>
    <div class="abs storage-note">
      Vegetable butters may melt or partially melt in transit.<br>
      Some butter may crystallize if they solidify too slowly.<br>
      This does not impact the quality of the butter.
    </div>
    <div class="abs company-info">
      <p>Distributed By Kavoro LLC<br>Brookfield, DE 19900</p>
      <p>Produced in Ghana By:<br>Amberleaf Ghana Ltd<br>www.amberleafgh.com</p>
    </div>
  </section>

</div>
</body>
</html>
```